Postcard Design

We provide humorous speechwriting and presentation coaching services, primarily for the wedding market (best man, father of the bride, maid of honor). We'd like a design that incoporates the blue and white logo colors into a nice overall design, with the pitch:
"Use the power of humor to deliver the BEST speech of your life!"
Target Market(s)
Wedding market (best man, bride/groom)
Industry/Entity Type
Wedding
Requirements
Must have
- Bulletpoints for services provided:
- Speechwriting
- Presentation Coaching
- Emcee & Officiant Services
Listing of benefits provided:
- Conquer stage fright
- Deliver your speech like a pro
- Be funny AND tactful
- Leave them wanting more
Contact info -
Trent Halvorsen
Trent@QuipCraftly.com
www.QuipCraftly.com
Testimonial quotes:
"People are STILL raving about that speech at our wedding. Thanks Quip Craftly!"
- Dana & Paul Fenwick, Baltimore, MD
"With the help of Quip Craftly, my best man speech brought down the house!"
- Mark Delahunt, Melville, NY

```html
<!DOCTYPE html>
<html lang="en">
<head>
<meta charset="utf-8">
<title>Quip Craftly Postcard</title>
<link rel="stylesheet" href="https://fonts.googleapis.com/css2?family=Josefin+Sans:wght@300&family=Open+Sans:wght@400&family=Tinos:wght@400;700&display=swap">
<style>
  :root {
    --navy: #1b2a52;
    --navy-deep: #16213f;
    --blue-bright: #1e90d8;
    --blue-mid: #1763a8;
    --blue-dark: #1c3768;
    --pill-edge: #3aa0e0;
    --white: #ffffff;
    --ink-soft: #3a3a3a;
    --photo-light: #f1ebe4;
    --photo-warm: #d9b89a;
    --photo-cool: #b9c7d8;
  }
  * { margin: 0; padding: 0; box-sizing: border-box; }
  html, body { width: 1200px; height: 924px; overflow: hidden; background: var(--white); }
  .postcard { position: relative; width: 1200px; height: 924px; overflow: hidden; }

  .hero-photo {
    position: absolute; left: 0; top: 0; width: 1200px; height: 600px;
    background:
      radial-gradient(ellipse 420px 260px at 250px 420px, rgba(217,184,154,.75), transparent 70%),
      radial-gradient(ellipse 380px 260px at 760px 380px, rgba(185,199,216,.8), transparent 70%),
      radial-gradient(ellipse 300px 220px at 1020px 440px, rgba(200,170,150,.6), transparent 70%),
      linear-gradient(180deg, var(--photo-light) 0%, #e8ddd2 60%, var(--photo-warm) 100%);
  }

  .contact-box {
    position: absolute; left: 0; top: 60px; width: 410px; height: 153px;
    background: var(--navy-deep); border-radius: 0 14px 14px 0;
    padding: 22px 0 0 61px;
    font-family: "Open Sans", sans-serif; font-size: 26px; line-height: 35px; color: var(--white);
  }

  .pitch {
    position: absolute; right: 60px; top: 78px; width: 560px;
    text-align: right; font-family: "Josefin Sans", sans-serif; font-weight: 300;
    font-size: 43px; line-height: 55px; color: var(--ink-soft);
  }

  .lower-band { position: absolute; left: 0; top: 0; width: 1200px; height: 924px; }

  .services { position: absolute; left: 62px; top: 602px; list-style: none; }
  .service-pill {
    position: relative; width: 574px; height: 68px; margin-bottom: 27px;
    border-radius: 34px; border: 3px solid var(--pill-edge);
    background: linear-gradient(180deg, #2c4a86 0%, var(--navy) 45%, var(--navy-deep) 100%);
    box-shadow: 3px 4px 0 #152038;
    padding-left: 32px;
    font-family: "Tinos", serif; font-size: 40px; line-height: 60px; color: var(--white);
  }

  .benefits { position: absolute; left: 682px; top: 596px; font-family: "Tinos", serif; color: var(--white); }
  .benefits-title { font-weight: 700; font-size: 28px; line-height: 34px; }
  .benefits-list { list-style: none; font-size: 32px; line-height: 38.5px; }
  .benefits-list li::before { content: "\2022"; margin-right: 8px; }
</style>
</head>
<body>
<div class="postcard">
  <div class="hero-photo" role="img" aria-label="Photo of a smiling audience in a seminar room raising their hands"></div>

  <svg class="lower-band" viewBox="0 0 1200 924" aria-hidden="true">
    <defs>
      <linearGradient id="bandFill" x1="0" y1="0" x2="1" y2="0">
        <stop offset="0" stop-color="var(--blue-bright)"/>
        <stop offset="0.5" stop-color="var(--blue-mid)"/>
        <stop offset="1" stop-color="var(--blue-dark)"/>
      </linearGradient>
    </defs>
    <path d="M0,570 C250,530 450,505 650,508 C880,512 1050,530 1200,550 L1200,924 L0,924 Z" fill="var(--white)"/>
    <path d="M0,586 C250,548 450,522 650,524 C880,528 1050,546 1200,566 L1200,924 L0,924 Z" fill="url(#bandFill)"/>
  </svg>

  <div class="contact-box">
    <p>Trent Halvorsen</p>
    <p>Trent@QuipCraftly.com</p>
    <p>www.QuipCraftly.com</p>
  </div>

  <p class="pitch">“Use the power of humor to deliver the BEST speech of your life!”</p>

  <ul class="services">
    <li class="service-pill">Speechwriting</li>
    <li class="service-pill">Presentation Coaching</li>
    <li class="service-pill">Emcee &amp; Officiant Services</li>
  </ul>

  <div class="benefits">
    <h2 class="benefits-title">BENEFITS</h2>
    <ul class="benefits-list">
      <li>Conquer stage fright</li>
      <li>Deliver your speech like a pro</li>
      <li>Be funny AND tactful</li>
      <li>Leave them wanting more</li>
    </ul>
  </div>
</div>
</body>
</html>
```